SilverLedgerOak - Double Sided Business Card

We are looking for design options or our business cards. We are a Business Solutions and HR solutions Provider - the theme is business, for this card.

Our brand colours are represented within our logo.

Details needed to be put on the front of the business card are:

Employees name: [Sample Name]
Role: [Sample Role]

Address: Suite 4 - Level 3/48 Halloran Avenue Parramatta NSW 2150
M: 0000 000 000
P: 1300 847 213
F: 1300 847 286
E: sample@silverledgeroak.com.au
www.silverledgeroak.com.au
Updates

Reason: Hello, could we please increase our deadline by 5 days. Thanking you, Tess

Target Market(s)

Business Owners, also Candidates looking for Employment

Industry/Entity Type

Business

Contact Information for Business Card

Role: [Sample Role]

M: 0000 000 000
P: 1300 847 213
F: 1300 847 286

Font styles to use
Sans Serif

Colors
3276b5
3176b5
0455a3
85abd2
cfdeed
ffffff
000000
1b1b1b
757575

Requirements
Must have
• Details needed to be put on the front of the business card are:
• Employees name: [Sample Name]
• Role: [Sample Role]
• Address: Suite 4 - Level 3/48 Halloran Avenue Parramatta NSW 2150
• M: 0000 000 000
• P: 1300 847 213
• F: 1300 847 286
• E: sample@silverledgeroak.com.au
• www.silverledgeroak.com.au
Nice to have
• Simplicity, clean and professional.

```html
<!DOCTYPE html>
<html lang="en">
<head>
<meta charset="utf-8">
<title>SilverLedgerOak Business Card</title>
<link rel="stylesheet" href="https://fonts.googleapis.com/css2?family=Arimo:wght@400;700&display=swap">
<style>
  :root {
    --stage: #2b2b2b;
    --card: #f4f5f7;
    --white: #ffffff;
    --brand-blue: #3176b5;
    --band-blue: #2e5f9e;
    --navy: #0f2a4f;
    --ink: #1b1b1b;
    --ink-navy: #14284a;
    --rule: #757575;
  }
  * { box-sizing: border-box; margin: 0; padding: 0; }
  html, body { width: 1200px; height: 997px; overflow: hidden; }
  body {
    background: var(--stage);
    font-family: "Arimo", Arial, sans-serif;
    position: relative;
  }
  .card {
    position: absolute;
    left: 250px;
    width: 700px;
    height: 400px;
    background: linear-gradient(180deg, var(--white) 0%, var(--card) 100%);
    border-radius: 22px;
    overflow: hidden;
  }
  .card--back { top: 60px; }
  .card--front { top: 520px; }

  .brand {
    position: absolute;
    left: 0; right: 0;
    text-align: center;
  }
  .brand__row {
    display: inline-flex;
    align-items: center;
    gap: 12px;
  }
  .brand__mark {
    width: 30px; height: 30px;
    background: var(--brand-blue);
  }
  .brand__name {
    font-weight: 700;
    font-size: 38px;
    color: var(--brand-blue);
    letter-spacing: 0.5px;
  }
  .brand__tagline {
    display: inline-block;
    margin-top: 6px;
    padding-top: 5px;
    border-top: 1px solid var(--rule);
    font-weight: 700;
    font-size: 12px;
    color: var(--ink);
  }
  .card--back .brand { top: 165px; }
  .card--front .brand { top: 72px; }

  .rule {
    position: absolute;
    left: 0; right: 0;
    height: 2px;
    background: var(--band-blue);
  }
  .rule--top { top: 182px; }
  .rule--bottom { top: 336px; }

  .contact-panel {
    position: absolute;
    left: 390px; right: 0;
    top: 188px; height: 142px;
    background: var(--navy);
    padding: 22px 0 0 48px;
  }
  .contact-list { list-style: none; }
  .contact-list li {
    display: flex;
    align-items: center;
    gap: 10px;
    color: var(--white);
    font-size: 15px;
    line-height: 23px;
    letter-spacing: 0.5px;
  }
  .contact-list svg { width: 15px; height: 15px; flex: none; }

  .person-panel {
    position: absolute;
    left: 0; width: 390px;
    top: 240px; height: 90px;
    background: var(--band-blue);
    padding: 22px 0 0 110px;
  }
  .person__name {
    font-weight: 700;
    font-size: 20px;
    color: var(--white);
    letter-spacing: 0.5px;
  }
  .person__role {
    font-weight: 700;
    font-size: 15px;
    color: var(--ink);
    margin-left: 46px;
  }

  .website {
    position: absolute;
    left: 0; right: 0;
    top: 356px;
    text-align: center;
    font-weight: 700;
    font-size: 18px;
    letter-spacing: 5px;
    color: var(--ink-navy);
  }
</style>
</head>
<body>

<section class="card card--back" aria-label="Business card back">
  <div class="brand">
    <div class="brand__row">
      <span class="brand__mark"></span>
      <span class="brand__name">SILVERLEDGEROAK</span>
    </div><br>
    <span class="brand__tagline">Supporting small and mid-size firms to reach their goals</span>
  </div>
</section>

<section class="card card--front" aria-label="Business card front">
  <div class="brand">
    <div class="brand__row">
      <span class="brand__mark"></span>
      <span class="brand__name">SILVERLEDGEROAK</span>
    </div><br>
    <span class="brand__tagline">Supporting small and mid-size firms to reach their goals</span>
  </div>

  <div class="rule rule--top"></div>

  <div class="contact-panel">
    <ul class="contact-list">
      <li>
        <svg viewBox="0 0 16 16" aria-hidden="true"><circle cx="8" cy="8" r="8" fill="#cfdeed"/><rect x="5.5" y="3" width="5" height="10" rx="1" fill="#0f2a4f"/></svg>
        0000 000 000
      </li>
      <li>
        <svg viewBox="0 0 16 16" aria-hidden="true"><circle cx="8" cy="8" r="8" fill="#cfdeed"/><path d="M4 6.5a4 2 0 0 1 8 0v1.5h-2.5v-1.2h-3v1.2H4z M5 9h6v3H5z" fill="#0f2a4f"/></svg>
        1300 847 213
      </li>
      <li>
        <svg viewBox="0 0 16 16" aria-hidden="true"><circle cx="8" cy="8" r="8" fill="#cfdeed"/><rect x="4" y="6" width="8" height="6" rx="1" fill="#0f2a4f"/><rect x="5.5" y="3.5" width="5" height="3" fill="#0f2a4f"/></svg>
        1300 847 286
      </li>
      <li>
        <svg viewBox="0 0 16 16" aria-hidden="true"><circle cx="8" cy="8" r="8" fill="#cfdeed"/><rect x="4" y="5" width="8" height="6" fill="#0f2a4f"/><path d="M4 5l4 3.5L12 5" stroke="#cfdeed" stroke-width="1" fill="none"/></svg>
        info@silverledgeroak.com.au
      </li>
    </ul>
  </div>

  <div class="person-panel">
    <p class="person__name">DANIEL MARSH</p>
    <p class="person__role">Director</p>
  </div>

  <div class="rule rule--bottom"></div>

  <p class="website">WWW.SILVERLEDGEROAK.COM.AU</p>
</section>

</body>
</html>
```